Velnadex a Canadian Brand

I'm looking for a new name card design together with our new brand "Velnadex"! FYI, Velnadex is a new developed compounds for raw plastic material in order to improve the Physical properties。

Target Market(s)

Worldwide

Industry/Entity Type

Plastic

```html
<!DOCTYPE html>
<html lang="en">
<head>
<meta charset="utf-8">
<title>Velnadex Business Card</title>
<link href="https://fonts.googleapis.com/css2?family=Open+Sans:wght@400;600;700&display=swap" rel="stylesheet">
<style>
  :root {
    --backdrop: #080808;
    --card-edge: #a7abab;
    --card-mid: #c4d1d1;
    --brand-red: #c0272d;
    --ink: #1c1c1e;
    --icon-fg: #ffffff;
  }
  * { margin: 0; padding: 0; box-sizing: border-box; }
  html, body {
    width: 1200px; height: 1000px; overflow: hidden;
    background: var(--backdrop);
    font-family: "Open Sans", Arial, sans-serif;
  }
  .canvas { position: relative; width: 1200px; height: 1000px; }
  .card {
    position: absolute; left: 274px; width: 651px; height: 381px;
    background: linear-gradient(180deg, var(--card-edge) 0%, var(--card-mid) 45%, var(--card-mid) 60%, var(--card-edge) 100%);
    overflow: hidden;
  }
  .card--front { top: 109px; }
  .card--back { top: 523px; }

  .brand {
    position: absolute; display: flex; align-items: center;
    color: var(--brand-red); font-weight: 700; letter-spacing: -1px; line-height: 1;
  }
  .brand__dot { border-radius: 50%; background: var(--brand-red); flex: none; }
  .card--front .brand { left: 0; right: 0; top: 154px; justify-content: center; font-size: 68px; gap: 14px; }
  .card--front .brand__dot { width: 34px; height: 34px; }
  .card--back .brand { left: 31px; top: 30px; font-size: 46px; gap: 10px; }
  .card--back .brand__dot { width: 24px; height: 24px; }

  .holder { position: absolute; right: 32px; top: 32px; text-align: right; line-height: 1; }
  .holder__name { color: var(--ink); font-weight: 700; font-size: 25px; letter-spacing: 0.5px; }
  .holder__role { color: var(--brand-red); font-weight: 600; font-size: 20px; margin-top: 3px; }

  .company { position: absolute; left: 27px; top: 224px; color: var(--ink); }
  .company__name { font-weight: 700; font-size: 19px; letter-spacing: 0.3px; }
  .company__address { font-size: 20px; margin-top: 1px; }

  .contacts { position: absolute; left: 29px; top: 286px; list-style: none; }
  .contacts li {
    display: flex; align-items: center; gap: 10px; height: 24.5px;
    color: var(--ink); font-weight: 600; font-size: 20px;
  }
  .contacts svg { width: 19px; height: 19px; flex: none; }
</style>
</head>
<body>
<main class="canvas">
  <section class="card card--front" aria-label="Card front">
    <div class="brand"><span>Velnadex</span><span class="brand__dot"></span></div>
  </section>

  <section class="card card--back" aria-label="Card back">
    <div class="brand"><span>Velnadex</span><span class="brand__dot"></span></div>

    <div class="holder">
      <div class="holder__name">JOHN DOE</div>
      <div class="holder__role">Director</div>
    </div>

    <div class="company">
      <div class="company__name">Velnadex Pty.Ltd.</div>
      <div class="company__address">P.O.Box 417 Marlowe Bay NSW 2159</div>
    </div>

    <ul class="contacts">
      <li>
        <svg viewBox="0 0 20 20" aria-hidden="true">
          <rect width="20" height="20" rx="2" fill="var(--brand-red)"/>
          <rect x="6" y="3" width="8" height="14" rx="1.5" fill="none" stroke="var(--icon-fg)" stroke-width="1.6"/>
          <circle cx="10" cy="14.3" r="0.9" fill="var(--icon-fg)"/>
        </svg>
        <span>0123 456 789</span>
      </li>
      <li>
        <svg viewBox="0 0 20 20" aria-hidden="true">
          <rect width="20" height="20" rx="2" fill="var(--brand-red)"/>
          <path d="M3.5 8 Q10 3 16.5 8 L15 10 L12.5 9 L12.5 7.5 Q10 6.8 7.5 7.5 L7.5 9 L5 10 Z" fill="var(--icon-fg)"/>
          <rect x="5" y="11" width="10" height="6" rx="1" fill="var(--icon-fg)"/>
          <circle cx="10" cy="14" r="1.6" fill="var(--brand-red)"/>
        </svg>
        <span>0123 456 789</span>
      </li>
      <li>
        <svg viewBox="0 0 20 20" aria-hidden="true">
          <rect width="20" height="20" rx="2" fill="var(--brand-red)"/>
          <rect x="3.5" y="5.5" width="13" height="9" fill="none" stroke="var(--icon-fg)" stroke-width="1.5"/>
          <path d="M3.5 5.5 L10 11 L16.5 5.5" fill="none" stroke="var(--icon-fg)" stroke-width="1.5"/>
        </svg>
        <span>hello@velnadex.example</span>
      </li>
    </ul>
  </section>
</main>
</body>
</html>
```